International Trading Company, 'KIRO' needs a Business Card

The company name is "KIRO" and it has own logo design.
I'd like to use its logo on this business card.
I need two side Business Card.
I'll look forward to your great design.
Thank you very much in advance.

Contact Information for Business Card

Company Name : Kiro Harbour Limited
Information Example
Dorian Pallister
Mobile(use icon please) : 1 (212) 555-0143
Tel(use icon please) : 1 (212) 555-0178
Email(use icon please) : dorian27@kiroharbour-mail.com
Address(use icon please) : 482 Halden Ave, New York, NY 10160, USA

```html
<!DOCTYPE html>
<html lang="en">
<head>
<meta charset="utf-8">
<title>KIRO Business Card</title>
<link rel="stylesheet" href="https://fonts.googleapis.com/css2?family=Roboto:wght@400;700;900&display=swap">
<style>
  :root {
    --backdrop: #2b2b2b;
    --card: #0b0b0b;
    --card-edge: #151515;
    --brand-grey: #5f5f60;
    --text-grey: #6a6a6a;
    --rule: #3e3e3e;
  }
  * { margin: 0; padding: 0; box-sizing: border-box; }
  html, body {
    width: 1200px;
    height: 1000px;
    overflow: hidden;
    background: var(--backdrop);
    font-family: "Roboto", Arial, sans-serif;
  }
  .card {
    position: absolute;
    left: 220px;
    width: 760px;
    background: var(--card);
    border: 1px solid var(--card-edge);
  }
  .card--front { top: 50px; height: 433px; }
  .card--back { top: 524px; height: 436px; }

  .brand-name {
    position: absolute;
    font-weight: 900;
    font-size: 78px;
    line-height: 1;
    letter-spacing: 2px;
    color: var(--brand-grey);
  }
  .card--front .brand-name { right: 43px; bottom: 37px; }
  .card--back .brand-name { left: 41px; top: 38px; }

  .holder-name {
    position: absolute;
    right: 43px;
    top: 245px;
    font-weight: 700;
    font-size: 19px;
    letter-spacing: 0.5px;
    color: var(--text-grey);
  }
  .divider {
    position: absolute;
    left: 42px;
    right: 43px;
    top: 281px;
    height: 1px;
    background: var(--rule);
  }
  .contact-list {
    position: absolute;
    left: 41px;
    top: 299px;
    list-style: none;
  }
  .contact-item {
    display: flex;
    align-items: center;
    height: 24.5px;
    font-size: 17px;
    color: var(--text-grey);
  }
  .contact-icon {
    width: 13px;
    height: 13px;
    margin-right: 5px;
    fill: var(--text-grey);
    flex: none;
  }
</style>
</head>
<body>
  <section class="card card--front">
    <div class="brand-name">KIRO</div>
  </section>

  <section class="card card--back">
    <div class="brand-name">KIRO</div>
    <div class="holder-name">DORIAN PALLISTER</div>
    <div class="divider"></div>
    <ul class="contact-list">
      <li class="contact-item">
        <svg class="contact-icon" viewBox="0 0 13 13" aria-hidden="true"><path d="M3.5 0h6a1 1 0 0 1 1 1v11a1 1 0 0 1-1 1h-6a1 1 0 0 1-1-1V1a1 1 0 0 1 1-1zm0.5 1.5v8.5h5V1.5zm2.5 9.3a0.8 0.8 0 1 0 0 1.6a0.8 0.8 0 1 0 0-1.6z" fill-rule="evenodd"/></svg>
        1 (212) 555-0143
      </li>
      <li class="contact-item">
        <svg class="contact-icon" viewBox="0 0 13 13" aria-hidden="true"><path d="M0.5 4.2C2 2.2 4.2 1.5 6.5 1.5s4.5 0.7 6 2.7l-0.4 1.6-2.4-0.6V3.9H3.3v1.3l-2.4 0.6zM2.5 7.5L4 5.5h5l1.5 2v4H2.5zm4 0.6a1.4 1.4 0 1 0 0 2.8a1.4 1.4 0 1 0 0-2.8z" fill-rule="evenodd"/></svg>
        1 (212) 555-0178
      </li>
      <li class="contact-item">
        <svg class="contact-icon" viewBox="0 0 13 13" aria-hidden="true"><path d="M1 3h11v7H1zm0.8 0.6L6.5 7.2l4.7-3.6z" fill-rule="evenodd"/></svg>
        dorian27@kiroharbour-mail.com
      </li>
      <li class="contact-item">
        <svg class="contact-icon" viewBox="0 0 13 13" aria-hidden="true"><path d="M6.5 0.5a4.2 4.2 0 0 1 4.2 4.2c0 3-4.2 7.8-4.2 7.8S2.3 7.7 2.3 4.7A4.2 4.2 0 0 1 6.5 0.5zm0 2.6a1.6 1.6 0 1 0 0 3.2a1.6 1.6 0 1 0 0-3.2z" fill-rule="evenodd"/></svg>
        482 Halden Ave, New York, NY 10160, USA
      </li>
    </ul>
  </section>
</body>
</html>
```